Flyer-Design für Buchhaltungsservice
Zielgruppe
Wir bieten Buchhaltungservice und Lohnbuchhaltungsservice an und möchten damit Kleinunternehmen ansprechen!
Aufgabenstellung
Ich habe ein Text zusammengestellt , dieser kann ergänzt oder geändert werden! Bin für Ideen offen! Diesen Text nutze ich aber schon sehr lange! Ich würde vl. noch die Unterschrift mit einfügen als Abspann! Ich bin am überlegen ob ich ein Foto von mir selbst einfüge, aber das alles würde ich gerne durch den Designer als Vorschlag haben. Bitte bei meinem Bild auch ein Ausschnitt verwenden, das Bild ist absolut unbearbeitet! Gerne auch schwarz/weiß!
Die Sterne müssen bei dem Wort dabei stehen und ganz unten findet sich die Erklärung, dies ist rechtlich sehr wichtig!
Es sollte ein Flyer gestaltet werden was später als Postkarte versendet werden kann siehe Anlage von morvadruck datenblatt, bitte so ein Flyer gestalten!

```html
<!DOCTYPE html>
<html lang="de">
<head>
<meta charset="utf-8">
<title>KONTELIS GmbH – Buchhaltung</title>
<link rel="stylesheet" href="https://fonts.googleapis.com/css2?family=Open+Sans:ital,wght@0,400;0,600;1,400&display=swap">
<style>
  :root {
    --brand-blue: #1070b8;
    --panel-blue: #bfcce9;
    --text-dark: #333a40;
    --white: #ffffff;
  }
  html, body { margin: 0; padding: 0; overflow: hidden; }
  body { width: 1120px; height: 1200px; background: var(--white); }
  .flyer {
    position: relative; width: 1120px; height: 1200px; overflow: hidden;
    font-family: "Open Sans", Arial, sans-serif; color: var(--text-dark);
  }
  .abs { position: absolute; }

  .claim-band {
    left: 0; top: 0; width: 1120px; height: 72px; background: var(--brand-blue);
    color: var(--white); font-size: 35px; line-height: 72px; text-align: center;
    letter-spacing: 0.5px; padding-left: 50px; box-sizing: border-box;
  }
  .portrait {
    left: 0; top: 72px; width: 618px; height: 526px;
    background: linear-gradient(100deg, #6e6e6e 0%, #cfcfcf 28%, #f2f2f2 50%, #e6c27a 72%, #bdbdbd 88%, #e9e9e9 100%);
  }
  .logo-box {
    left: 317px; top: 72px; width: 243px; height: 110px; background: var(--brand-blue);
    display: flex; flex-direction: column; align-items: center; justify-content: center; gap: 8px;
  }
  .brand-mark { width: 30px; height: 30px; background: var(--white); }
  .brand-name { color: var(--white); font-size: 29px; letter-spacing: 1.5px; }
  .service-panel {
    left: 560px; top: 72px; width: 560px; height: 110px; background: var(--panel-blue);
  }
  .service-title {
    left: 0; top: 2px; width: 100%; text-align: center;
    color: var(--brand-blue); font-size: 40px;
  }
  .service-list { left: 14px; top: 62px; font-size: 21px; white-space: nowrap; }
  .service-note { left: 351px; top: 88px; font-size: 13.5px; font-style: italic; }

  .lead { color: var(--brand-blue); font-style: italic; font-size: 22.5px; margin: 0; font-weight: 400; }
  .body-copy { font-size: 17px; line-height: 24px; margin: 0; }

  .intro { left: 642px; top: 192px; width: 460px; }
  .intro .lead { margin-bottom: 20px; }
  .intro .body-copy { margin-bottom: 11px; }
  .intro .lead.second { margin-top: 14px; margin-bottom: 20px; }
  .intro .lead.third { margin-top: 12px; }

  .offer { left: 26px; top: 615px; width: 640px; }
  .offer .lead { font-size: 23px; line-height: 31px; }
  .benefits { list-style: none; margin: 8px 0 0; padding: 0; font-size: 17.5px; line-height: 24px; }
  .benefits li { position: relative; padding-left: 19px; }
  .benefits li::before {
    content: ""; position: absolute; left: 2px; top: 10px; width: 5px; height: 5px;
    border-radius: 50%; background: var(--brand-blue);
  }
  .closing { margin-top: 12px; }

  .signature {
    left: 240px; top: 936px; width: 112px; height: 90px;
    background: linear-gradient(135deg, #f7f7f7, #ececec);
  }
  .greeting { left: 27px; top: 910px; font-size: 17px; white-space: nowrap; }
  .signer { left: 27px; top: 937px; font-size: 22px; white-space: nowrap; }
  .footnote { left: 27px; top: 1038px; font-size: 11.5px; line-height: 16px; }

  .footer-band {
    left: 0; top: 1080px; width: 688px; height: 120px; background: var(--brand-blue); color: var(--white);
  }
  .footer-logo {
    left: 8px; top: 14px; width: 180px; display: flex; flex-direction: column; align-items: center; gap: 8px;
  }
  .footer-logo .brand-name { font-size: 27px; }
  .footer-contact { left: 209px; top: 14px; font-size: 18px; line-height: 24px; }

  .recipient { left: 714px; top: 940px; font-size: 19.5px; line-height: 28px; color: #111; }
</style>
</head>
<body>
<div class="flyer">
  <div class="abs claim-band">ZUVERLÄSSIG &nbsp;•&nbsp; DISKRET &nbsp;•&nbsp; PROFESSIONELL</div>

  <div class="abs portrait" role="img" aria-label="Schwarz-weiß Porträtfoto des Buchhalters am Schreibtisch mit goldener Tischlampe"></div>

  <div class="abs logo-box">
    <div class="brand-mark"></div>
    <div class="brand-name">KONTELIS</div>
  </div>

  <div class="abs service-panel">
    <div class="abs service-title">Buchhaltung</div>
    <div class="abs service-list">•&nbsp; mit Hol- und Bringservice •&nbsp; lfd. Lohnbuchhaltung</div>
    <div class="abs service-note">(auch Baulohn)</div>
  </div>

  <div class="abs intro">
    <h2 class="lead">Mit Sicherheit kennen Sie die Situation:</h2>
    <p class="body-copy">Sie bekommen die Buchhaltungsunterlagen zurück und es fehlt die Zeit diese zu besprechen!</p>
    <p class="body-copy">Vermissen Sie nicht auch manchmal die persönliche Betreuung?</p>
    <h2 class="lead second">Dann stellen Sie sich folgende Situation vor:</h2>
    <p class="body-copy">Ihr persönlicher Buchhalter* holt die Unterlagen<br>kostenlos durch einen Kurier bei Ihnen ab,<br>bucht sie und druckt anschließend die entsprechenden<br>betriebswirtschaftlichen Belege aus und<br>Sie bekommen die Auswertungen ausführlich erläutert.</p>
    <h2 class="lead third">Dieser Service ist möglich!</h2>
  </div>

  <div class="abs offer">
    <h2 class="lead">Rufen Sie mich noch heute an, um so schnell wie möglich von meinen Leistungen zu profitieren:</h2>
    <ul class="benefits">
      <li>Ein Dienstleister für das Buchen der lfd. Geschäftsvorfälle<br>der Finanzbuchhaltung und lfd. Lohnbuchhaltung</li>
      <li>Immer gleicher Ansprechpartner</li>
      <li>Persönliche und qualifizierte Betreuung</li>
      <li>Hol- und Bringservice</li>
      <li>auch komplett digitale Buchhaltung* möglich</li>
    </ul>
    <h2 class="lead closing">Sie haben endlich eine Buchhalter* als Ansprechpartner, der Sie sofort entlastet.</h2>
  </div>

  <div class="abs signature" role="img" aria-label="Handschriftliche Unterschrift"></div>
  <div class="abs greeting">Mit freundlichen Grüßen</div>
  <div class="abs signer">Jonas Ferwald</div>

  <div class="abs footnote">*Mein Dienstleistungsangebot in der Buchhaltung umfasst ausschließlich das Buchen lfd.<br>Geschäftsvorfälle, die lfd. Lohnabrechnung und das Fertigen der Lohnsteueranmeldung</div>

  <div class="abs footer-band">
    <div class="abs footer-logo">
      <div class="brand-mark"></div>
      <div class="brand-name">KONTELIS</div>
    </div>
    <div class="abs footer-contact">
      KONTELIS GmbH<br>
      Lindenkamp 14 &nbsp;•&nbsp; 73210 Talbrunn<br>
      Telefon: 0150 / 123 456 78 &nbsp;•&nbsp; Email: info@kontelis.de<br>
      www.kontelis.de
    </div>
  </div>

  <div class="abs recipient">FIrma<br>Firma 2<br>Vorname Nachname<br>Straße<br>Ort<br>Land</div>
</div>
</body>
</html>
```